UI Kit for Contractor Websites

I created a wireframe in Webflow and want to create a number of templates around that. There are existing templates, but I a few built around my content structure.

The types of clients are home remodeling services (homebuilders, plumbers, painters, electricians, handymen, etc.)

https://site-draft-7bc41d92e30-fd19a2b84c07e.pagehost.example/

*Use the website copy content from here but you do NOT need to follow the wireframe so plug it in however you feel best. Eventually, we'll have multiple types of heroes, services, etc.

I'd like to start with the first homepage template. The homepage templates will all have the same fonts, color scheme, and content. Once we finish about 5 of those, we'd move onto the next stage.

https://www.clipvault.example/share/5d8e0b31f7a249c6b0e2a9f41c7d3e88

Other clean, modern, UI kits (templates) or websites I like:
https://www.brimlow.example/
https://vector-layout.pagehost.example/
https://quillet.example/
https://tern-layout.pagehost.example/
https://www.plotnest.example/talebrick-website-templates
https://relay-layout.pagehost.example/
https://tiles-layout.pagehost.example/

*We'd likely have a lot of images, not illustrations since the client type we're building is pretty visual. Can use dummy photos.

Home

Navbar

Hero Section
Preheader (H1)
Hero Header (H2)
Hero CTA
Hero Secondary CTA

Hero Testimonial Short Quote
Hero Testimonial Name

Social Proof (CMS, can be multiple or one)
Testimonial Quote
Testimonial Name
Testimonial Image

CTA
CTA Headline
CTA Subheadline
CTA Button

Features/Value Stack
Value Stack H2
Value 1 Headline (H3)
Value 1 Description
Value 2 Headline (H3)
Value 2 Description
Value 3 Headline (H3)
Value 3 Description

Services (CMS, can be multiple)
Service Name
Service Short Description
CTA: Get Quote
Main Image

Homepage How It Works
Homepage How It Works Headline
How it Works Subheadline
Step 1 Name
Step 1 Description
Step 2 Name
Step 2 Description
Step 3 Name
Step 3 Description

About/Founder’s Note/Team
Homepage Founder Note Headline
Founder Note or About Info
Owner Signature
CTA to About Page

CTA
CTA Headline
CTA Subheadline
CTA Button

Footer

```html
<!DOCTYPE html>
<html lang="en">
<head>
<meta charset="utf-8">
<title>Contractor Homepage Template</title>
<link href="https://fonts.googleapis.com/css2?family=Playfair+Display:wght@600;700&family=Poppins:ital,wght@0,400;0,500;0,600;1,400&display=swap" rel="stylesheet">
<style>
:root{
  --yellow:#F5B31B;
  --yellow-deep:#E2A10F;
  --yellow-soft:#FBE3A6;
  --ink:#1F1F1F;
  --muted:#6F6F6F;
  --line:#E6E6E6;
  --backdrop:#DDE2E2;
  --white:#FFFFFF;
}
*{box-sizing:border-box;margin:0;padding:0}
html,body{width:1200px;height:4511px;overflow:hidden}
body{background:var(--backdrop);font-family:'Poppins',sans-serif;color:var(--ink);position:relative}
.page{position:absolute;left:49px;top:46px;width:1093px;height:4418px;background:var(--white);overflow:hidden}
.abs{position:absolute}
.serif{font-family:'Playfair Display',serif;font-weight:700;color:var(--ink)}
.btn{position:absolute;display:flex;align-items:center;justify-content:center;border-radius:30px;font-size:13px;font-weight:500;color:var(--ink);background:var(--yellow);box-shadow:0 10px 18px rgba(245,179,27,.35)}
.btn-outline{background:var(--white);border:1.5px solid var(--yellow-soft);color:var(--yellow);box-shadow:none}
.underline{position:absolute;height:2px;width:72px;background:var(--yellow)}
.glow{position:absolute;border-radius:50%;background:radial-gradient(circle,rgba(245,179,27,.28),rgba(245,179,27,0) 70%)}
.body-text{font-size:12px;line-height:19px;color:var(--muted)}
.card{position:absolute;background:var(--white);border-radius:8px;box-shadow:0 4px 22px rgba(0,0,0,.08)}
.photo{position:absolute}
/* nav */
.brand{position:absolute;left:79px;top:40px;display:flex;align-items:center;gap:10px;font-size:15px;font-weight:600;color:var(--yellow)}
.brand-mark{width:26px;height:26px;border-radius:50%;background:var(--yellow)}
.nav a{position:absolute;top:44px;font-size:12px;color:#555;text-decoration:none;letter-spacing:.3px}
.nav a.active{color:var(--yellow)}
/* values */
.value-card{top:777px;width:296px;height:216px;text-align:center}
.icon-ring{position:absolute;border-radius:50%;background:var(--yellow);border:3px solid var(--white);box-shadow:0 0 0 2px var(--yellow);display:flex;align-items:center;justify-content:center}
.value-card h3{position:absolute;top:105px;width:100%;font-size:16px;font-weight:500}
.value-card p{position:absolute;top:135px;left:26px;right:26px;font-size:11px;line-height:17px;color:var(--muted)}
/* struggle list */
.struggle-item{position:absolute;left:555px;width:460px;font-size:12px;color:var(--muted);border-bottom:1px solid var(--line);padding-bottom:16px}
/* testimonials */
.quote-card{top:1738px;width:260px;height:175px;border:1px solid var(--line);border-radius:4px;background:var(--white)}
.quote-card .avatar{position:absolute;left:92px;top:-38px;width:76px;height:76px;border-radius:50%;border:3px solid var(--yellow);background:linear-gradient(160deg,#6b4a3a,#d9b59a)}
.quote-card .mark{position:absolute;left:16px;top:52px;font-family:'Playfair Display',serif;font-size:22px;color:var(--yellow)}
.quote-card p{position:absolute;left:40px;right:20px;top:58px;font-size:12px;line-height:19px;color:var(--muted)}
.quote-card .name{position:absolute;left:40px;top:118px;font-size:12px;font-weight:600}
.quote-card .role{position:absolute;left:40px;top:138px;font-size:12px;font-style:italic;color:var(--muted)}
.dot{position:absolute;top:1939px;width:8px;height:8px;border-radius:50%;background:#D5D5D5}
/* services */
.service-card{top:2146px;width:287px;height:371px;overflow:hidden}
.service-card .photo{left:0;top:0;width:100%;height:159px}
.service-card .icon-ring{left:106px;top:121px;width:76px;height:76px;background:var(--white);border:2px solid var(--yellow);box-shadow:none}
.service-card h3{position:absolute;left:22px;top:214px;font-size:16px;font-weight:600}
.service-card p{position:absolute;left:22px;right:18px;top:246px;font-size:11px;line-height:17px;color:var(--muted)}
.service-card .btn{left:22px;top:313px;width:112px;height:34px;font-size:11px;box-shadow:none}
/* steps */
.step{position:absolute;left:666px;width:352px;height:105px;padding:22px 16px}
.step h4{font-size:13px;font-weight:600;margin-bottom:10px}
.step p{font-size:12px;line-height:18px;color:var(--muted)}
.step.active{border:2px solid var(--yellow)}
.step-dot{position:absolute;left:631px;width:14px;height:14px;border-radius:50%;background:#D8D8D8}
/* footer */
.footer-col{position:absolute;top:4108px;font-size:11px;color:#3a2a00}
.footer-col h5{font-size:11px;font-weight:600;margin-bottom:18px}
.footer-col li{list-style:none;margin-bottom:12px}
.field{position:absolute;left:753px;width:256px;height:32px;background:var(--white);border-radius:3px;font-size:10px;color:#B8B8B8;padding:9px 8px}
.social{width:26px;height:26px;background:#2a1f00;border-radius:4px;display:inline-block;margin-right:20px}
</style>
</head>
<body>
<div class="page">

  <!-- Navbar -->
  <div class="brand"><span class="brand-mark"></span>CompanyName</div>
  <nav class="nav">
    <a class="active" style="left:482px">HOME</a>
    <a style="left:569px">PLANNING &#8964;</a>
    <a style="left:706px">OUR WORKS</a>
    <a style="left:837px">ABOUT US</a>
    <a style="left:951px">CONTACT</a>
  </nav>

  <!-- Hero -->
  <div class="glow" style="left:60px;top:110px;width:380px;height:300px"></div>
  <h1 class="serif abs" style="left:77px;top:208px;font-size:52px;line-height:61px">Build Your<br>Dream Home.</h1>
  <p class="abs" style="left:77px;top:347px;width:420px;font-size:12px;line-height:18px;color:#444">we are proud to bring our more than 10 years of experience, wide variety of plans &amp; commitment to value as we help you design the new home solution you didn't know existed.</p>
  <div class="btn" style="left:77px;top:436px;width:160px;height:40px">Learn more &nbsp;›</div>
  <div class="btn btn-outline" style="left:252px;top:436px;width:162px;height:40px">Our works</div>

  <svg class="abs" style="left:608px;top:144px" width="400" height="400" viewBox="0 0 400 400">
    <circle cx="207" cy="199" r="193" fill="none" stroke="var(--yellow)" stroke-width="5"/>
    <circle cx="207" cy="199" r="175" fill="var(--yellow)"/>
  </svg>
  <div class="photo" role="img" aria-label="Photo of a modern brick and timber apartment building" style="left:647px;top:218px;width:340px;height:300px;border-radius:0 0 170px 170px / 0 0 150px 150px;background:linear-gradient(180deg,#b9c9d6 0%,#a07a5e 45%,#c0704c 100%)"></div>
  <div class="photo" role="img" aria-label="Photo of a large suburban house" style="left:897px;top:173px;width:116px;height:116px;border-radius:50%;border:4px solid var(--yellow);background:linear-gradient(180deg,#a9c6e3,#e8e8ea 55%,#6e9a4a)"></div>
  <div class="photo" role="img" aria-label="Photo of a modern house lit at dusk" style="left:618px;top:406px;width:116px;height:116px;border-radius:50%;border:4px solid var(--yellow);background:linear-gradient(180deg,#2c4f86,#4a6fa6 55%,#c9a46a)"></div>
  <div class="card" style="left:547px;top:203px;width:201px;height:80px;border-radius:4px">
    <span class="abs" style="left:12px;top:8px;font-family:'Playfair Display',serif;color:var(--yellow);font-size:16px">“</span>
    <p class="abs" style="left:32px;top:12px;font-size:9px;line-height:14px;color:#444">They are very recommended.<br>10 out of 10 works.</p>
    <span class="abs" style="left:30px;top:48px;width:22px;height:22px;border-radius:50%;background:#c9a58d" role="img" aria-label="Reviewer portrait"></span>
    <span class="abs" style="left:60px;top:50px;font-size:8px;font-weight:600">Dana Hale</span>
    <span class="abs" style="left:60px;top:61px;font-size:8px;color:var(--yellow);letter-spacing:1px">★★★★★</span>
  </div>

  <!-- Values -->
  <h2 class="serif abs" style="left:0;width:1093px;text-align:center;top:680px;font-size:32px">Our values.</h2>
  <div class="underline" style="left:510px;top:730px"></div>
  <div class="card value-card" style="left:77px">
    <div class="icon-ring" style="left:116px;top:23px;width:64px;height:64px"><svg width="28" height="28" viewBox="0 0 24 24" fill="none" stroke="#fff" stroke-width="1.6"><path d="M3 11l9-7 9 7v9H3z"/><path d="M10 20v-6h4v6"/></svg></div>
    <h3>Value 1</h3>
    <p>Lorem ipsum dolor sit amet, consectetur adipiscing elit, sed do eiusmod tempor incididunt ut labore et dolore magna.</p>
  </div>
  <div class="card value-card" style="left:399px">
    <div class="icon-ring" style="left:116px;top:23px;width:64px;height:64px"><svg width="28" height="28" viewBox="0 0 24 24" fill="none" stroke="#fff" stroke-width="1.6"><path d="M3 11l9-7 9 7v9H3z"/><path d="M10 20v-6h4v6"/></svg></div>
    <h3>Value 2</h3>
    <p>Lorem ipsum dolor sit amet, consectetur adipiscing elit, sed do eiusmod tempor incididunt ut labore et dolore magna.</p>
  </div>
  <div class="card value-card" style="left:722px">
    <div class="icon-ring" style="left:116px;top:23px;width:64px;height:64px"><svg width="28" height="28" viewBox="0 0 24 24" fill="none" stroke="#fff" stroke-width="1.6"><path d="M3 11l9-7 9 7v9H3z"/><path d="M10 20v-6h4v6"/></svg></div>
    <h3>Value 3</h3>
    <p>Lorem ipsum dolor sit amet, consectetur adipiscing elit, sed do eiusmod tempor incididunt ut labore et dolore magna.</p>
  </div>

  <!-- Struggles -->
  <span class="abs" style="left:77px;top:1102px;width:92px;height:46px;border-radius:46px 46px 0 0;background:#F1ECE1"></span>
  <span class="abs" style="left:347px;top:1152px;width:44px;height:44px;border-radius:0 44px 0 0;background:#FAEFD3"></span>
  <div class="abs" style="left:77px;top:1222px;width:349px;height:270px;border-radius:0 50px 50px 0;background:linear-gradient(180deg,var(--yellow),var(--yellow-deep))"></div>
  <div class="photo" role="img" aria-label="Photo of a white modular apartment tower" style="left:77px;top:1160px;width:250px;height:332px;background:linear-gradient(160deg,#f4f4f4,#cfd3d6 60%,#9aa2a8);clip-path:polygon(20% 0,100% 8%,100% 100%,0 100%,0 18%)"></div>
  <div class="glow" style="left:640px;top:1040px;width:320px;height:260px"></div>
  <h2 class="serif abs" style="left:555px;top:1114px;font-size:32px;line-height:40px">Do you struggle<br>with these?</h2>
  <div class="underline" style="left:555px;top:1206px"></div>
  <p class="struggle-item" style="top:1242px;line-height:19px">Lorem ipsum dolor sit amet, consectetur adipiscing elit, sed do eiusmod tempor incididunt ut labore et dolore magna aliqua.</p>
  <p class="struggle-item" style="top:1298px">Lorem ipsum dolor sit amet, consectetur adipiscing elit.</p>
  <p class="struggle-item" style="top:1355px">Lorem ipsum dolor sit amet, consectetur adipiscing elit.</p>
  <p class="struggle-item" style="top:1412px">Lorem ipsum dolor sit amet, consectetur adipiscing elit.</p>
  <p class="struggle-item" style="top:1469px">Lorem ipsum dolor sit amet, consectetur adipiscing elit.</p>
  <div class="btn" style="left:548px;top:1539px;width:153px;height:41px">Learn more &nbsp;›</div>

  <!-- Social proof -->
  <div class="glow" style="left:60px;top:1600px;width:320px;height:240px"></div>
  <h2 class="serif abs" style="left:77px;top:1716px;font-size:32px;line-height:41px">Hear what others<br>are saying</h2>
  <div class="underline" style="left:77px;top:1800px"></div>
  <p class="abs" style="left:77px;top:1823px;width:345px;font-size:12px;line-height:19px;color:#444">Lorem ipsum dolor sit amet, consectetur adipiscing elit, sed do eiusmod tempor incididunt ut labore.</p>
  <div class="btn" style="left:77px;top:1899px;width:132px;height:42px">View all</div>
  <div class="quote-card abs" style="left:478px">
    <span class="avatar" role="img" aria-label="Customer portrait"></span>
    <span class="mark">“</span>
    <p>Lorem ipsum dolor sit amet, consectetur adipiscing elit,</p>
    <span class="name">Marla T.</span>
    <span class="role">Head of Design, Northvane</span>
  </div>
  <div class="quote-card abs" style="left:759px">
    <span class="avatar" role="img" aria-label="Customer portrait"></span>
    <span class="mark">“</span>
    <p>Lorem ipsum dolor sit amet, consectetur adipiscing elit,</p>
    <span class="name">Marla T.</span>
    <span class="role">Head of Design, Northvane</span>
  </div>
  <span class="dot" style="left:717px;background:var(--yellow)"></span>
  <span class="dot" style="left:743px"></span>
  <span class="dot" style="left:769px"></span>

  <!-- Services -->
  <h2 class="serif abs" style="left:0;width:1093px;text-align:center;top:2048px;font-size:32px">What we offer.</h2>
  <div class="card service-card" style="left:77px">
    <div class="photo" role="img" aria-label="Photo of a landscaped garden lawn with shrubs" style="background:linear-gradient(180deg,#3f6b2a,#6fae3c 55%,#4f8c2a)"></div>
    <div class="icon-ring"><svg width="30" height="30" viewBox="0 0 24 24" fill="none" stroke="var(--yellow)" stroke-width="1.5"><path d="M12 20c-5 0-8-4-8-8 4 0 8 3 8 8zm0 0c5 0 8-4 8-8-4 0-8 3-8 8zm0 0V8"/></svg></div>
    <h3>Lanscaping</h3>
    <p>Lorem ipsum dolor sit amet, consectetur adipiscing elit, sed do eiusmod tempor incididunt ut labore et dolore magna.</p>
    <div class="btn">Learn more</div>
  </div>
  <div class="card service-card" style="left:403px">
    <div class="photo" role="img" aria-label="Photo of an empty white room with a ladder and paint roller" style="background:linear-gradient(180deg,#f1f1f1,#d9d9d9 70%,#4a4a4a)"></div>
    <div class="icon-ring"><svg width="30" height="30" viewBox="0 0 24 24" fill="none" stroke="var(--yellow)" stroke-width="1.5"><rect x="5" y="4" width="12" height="5" rx="1"/><path d="M17 6h2v5h-7v3"/><rect x="10.5" y="14" width="3" height="6" rx="1"/></svg></div>
    <h3>Painting</h3>
    <p>Lorem ipsum dolor sit amet, consectetur adipiscing elit, sed do eiusmod tempor incididunt ut labore et dolore magna.</p>
    <div class="btn">Learn more</div>
  </div>
  <div class="card service-card" style="left:730px">
    <div class="photo" role="img" aria-label="Photo of a tradesman cutting material with a saw" style="background:linear-gradient(160deg,#d9dde0,#8e99a3 55%,#3e5a86)"></div>
    <div class="icon-ring"><svg width="30" height="30" viewBox="0 0 24 24" fill="none" stroke="var(--yellow)" stroke-width="1.5"><path d="M14 4l6 6-3 3-6-6zM11 7L4 14l6 6 7-7"/></svg></div>
    <h3>Plumbing</h3>
    <p>Lorem ipsum dolor sit amet, consectetur adipiscing elit, sed do eiusmod tempor incididunt ut labore et dolore magna.</p>
    <div class="btn">Learn more</div>
  </div>

  <!-- How it works -->
  <div class="glow" style="left:700px;top:2560px;width:340px;height:260px"></div>
  <h2 class="serif abs" style="left:735px;top:2648px;font-size:32px">How it works.</h2>
  <div class="underline" style="left:740px;top:2698px"></div>
  <div class="photo" role="img" aria-label="Photo of hands choosing from a paint colour swatch fan" style="left:253px;top:2708px;width:213px;height:138px;border-radius:0 38px 0 0;background:linear-gradient(150deg,#2f3f4a,#bcc6cc 45%,#e9dcc8)"></div>
  <div class="photo" role="img" aria-label="Photo of a dim dining room with pendant lamps" style="left:77px;top:2804px;width:163px;height:246px;border-radius:38px 0 0 0;background:linear-gradient(180deg,#4b4b4b,#2d2a28 60%,#6a5a4c)"></div>
  <div class="photo" role="img" aria-label="Photo of workers on construction scaffolding" style="left:253px;top:2860px;width:227px;height:190px;border-radius:0 0 38px 0;background:linear-gradient(170deg,#c9d6e3,#9a7455 50%,#6a4a36)"></div>
  <span class="abs" style="left:637px;top:2748px;width:2px;height:270px;background:var(--line)"></span>
  <span class="step-dot" style="top:2741px;background:var(--yellow)"></span>
  <span class="step-dot" style="top:2860px"></span>
  <span class="step-dot" style="top:2979px"></span>
  <div class="card step active" style="top:2740px"><h4>Get a quote</h4><p>Lorem ipsum dolor sit amet, consectetur adipiscing elit, sed do eiusmod tempor.</p></div>
  <div class="card step" style="top:2859px"><h4>We do the job</h4><p>Lorem ipsum dolor sit amet, consectetur adipiscing elit, sed do eiusmod tempor.</p></div>
  <div class="card step" style="top:2978px"><h4>Show off your house</h4><p>Lorem ipsum dolor sit amet, consectetur adipiscing elit, sed do eiusmod tempor.</p></div>

  <!-- Founder note -->
  <div class="abs" style="left:0;top:3160px;width:1093px;height:442px;background:var(--yellow)"></div>
  <div class="photo" role="img" aria-label="Photo of a lit modern house facade at evening" style="left:406px;top:3160px;width:687px;height:442px;background:linear-gradient(90deg,var(--yellow) 0%,rgba(245,179,27,.75) 30%,#c9a64a 65%,#8fa58f 100%)"></div>
  <h2 class="serif abs" style="left:80px;top:3262px;font-size:32px;line-height:41px">Hear what others<br>are saying</h2>
  <div class="underline" style="left:80px;top:3347px;background:var(--ink)"></div>
  <p class="abs" style="left:80px;top:3370px;width:345px;font-size:12px;line-height:19px">Lorem ipsum dolor sit amet, consectetur adipiscing elit, sed do eiusmod tempor incididunt ut labore.</p>
  <p class="abs" style="left:80px;top:3442px;font-size:12px;font-weight:600">Nora K.</p>
  <p class="abs" style="left:80px;top:3462px;font-size:12px">Founder &amp; owner</p>
  <div class="btn" style="left:77px;top:3509px;width:184px;height:40px;background:var(--white);box-shadow:none;font-size:14px">Meet the team</div>

  <!-- CTA -->
  <h2 class="serif abs" style="left:0;width:1093px;text-align:center;top:3648px;font-size:32px">Ready to start?</h2>
  <p class="abs" style="left:0;width:1093px;text-align:center;top:3716px;font-size:12px;font-weight:500;color:#444">So are we. Let's Go!</p>
  <p class="abs" style="left:210px;width:673px;text-align:center;top:3755px;font-size:12px;line-height:19px;color:#555">Lorem ipsum dolor sit amet, consectetur adipiscing elit, sed do eiusmod tempor incididunt ut labore. Lorem ipsum dolor sit amet, consectetur adipiscing elit, sed do eiusmod tempor incididunt ut labore.</p>
  <div class="btn" style="left:466px;top:3857px;width:160px;height:41px;font-size:14px">Get started</div>

  <!-- Footer -->
  <svg class="abs" style="left:0;top:3940px" width="1093" height="478" viewBox="0 0 1093 478" preserveAspectRatio="none">
    <defs><linearGradient id="footerFill" x1="0" y1="0" x2="0" y2="1"><stop offset="0" stop-color="var(--yellow)"/><stop offset="1" stop-color="var(--yellow-deep)"/></linearGradient></defs>
    <path d="M0 40 C180 -10 330 0 560 60 C760 110 930 70 1093 20 L1093 478 L0 478 Z" fill="url(#footerFill)"/>
  </svg>
  <div class="abs" style="left:98px;top:4058px;display:flex;align-items:center;gap:10px;font-size:15px;font-weight:600;color:#2a1f00"><span style="width:22px;height:22px;border-radius:50%;background:#2a1f00"></span>Company</div>
  <div class="footer-col" style="left:98px"><h5>Connect with us :</h5><span class="social"></span><span class="social"></span><span class="social"></span></div>
  <div class="footer-col" style="left:315px"><h5>About :</h5><ul><li>Home</li><li>Planning</li><li>Gallery</li><li>Happy Customers</li><li>About Us</li></ul></div>
  <div class="footer-col" style="left:531px"><h5>Support :</h5><ul><li>FAQ's</li><li>Contact Us</li><li>Terms of Services</li><li>Privacy Declaration</li></ul></div>
  <div class="footer-col" style="left:753px;width:260px"><h5>Stay in Touch</h5><p style="line-height:16px">Get our latest news and newsletter. Build your dream house now.</p></div>
  <div class="field" style="top:4187px">Full name</div>
  <div class="field" style="top:4234px">Email address</div>
  <div class="abs" style="left:753px;top:4292px;width:256px;height:32px;background:#C88F0C;border-radius:3px;display:flex;align-items:center;justify-content:center;font-size:11px;font-weight:600;color:var(--white)">Sign Up</div>
  <span class="abs" style="left:80px;top:4369px;width:933px;height:1px;background:rgba(0,0,0,.15)"></span>
  <p class="abs" style="left:0;width:1093px;text-align:center;top:4388px;font-size:10px;font-weight:600;color:#2a1f00">© Company 2021 &nbsp;| &nbsp;All rights reserved</p>
</div>
</body>
</html>
```